Brightwater Ledger Services, Inc.

Tax, Accounting and Bookkeeping Services

“We provide our services, with you next mortgage in mind”

Special pricing available for all Mortgage Loan Customers!!

President / CEO Marcus Delaney

Primary service provider with over 27 years of experience

Call directly for more information: (240) 555-0182

Or email at: mdelaney@brightwaterledger-example.com

```html
<!DOCTYPE html>
<html lang="en">
<head>
<meta charset="utf-8">
<title>Brightwater Ledger Services – Tax, Accounting & Bookkeeping</title>
<link href="https://fonts.googleapis.com/css2?family=Libre+Baskerville:ital,wght@0,400;0,700;1,400&family=Montserrat:wght@500;600;700&display=swap" rel="stylesheet">
<style>
  :root{
    --frame:#0f1f3a;
    --navy:#14244a;
    --navy-deep:#0c1834;
    --cream:#f4ead4;
    --gold:#d8b66a;
    --gold-bright:#f0d693;
    --gold-dark:#a8843f;
    --ink:#14213f;
  }
  *{margin:0;padding:0;box-sizing:border-box}
  html,body{width:1200px;height:1173px;overflow:hidden;background:var(--frame)}
  .ad{position:absolute;left:95px;top:82px;width:1009px;height:1009px;overflow:hidden;
      background:radial-gradient(ellipse at 40% 60%,#1d3263 0%,var(--navy) 45%,var(--navy-deep) 100%)}
  .abs{position:absolute}
  .brand-area{left:0;top:0;width:700px;height:172px;
      background:linear-gradient(180deg,#cfc9bd 0%,#e2ddd2 55%,#c9c1b0 100%)}
  .brand{left:0;width:660px;top:62px;display:flex;justify-content:center;align-items:center;gap:12px}
  .brand-dot{width:22px;height:22px;border-radius:50%;background:var(--navy)}
  .brand-name{font-family:"Libre Baskerville",serif;font-weight:700;font-size:26px;color:var(--navy)}
  .rule{height:4px;background:linear-gradient(90deg,var(--gold-dark),var(--gold-bright),var(--gold-dark))}
  .tick{left:38px;top:199px}
  .headline{left:110px;top:192px;font-family:"Libre Baskerville",serif;font-weight:700;
      font-size:48px;line-height:62px;color:var(--cream)}
  .headline .l2{margin-left:-24px}
  .quote-band{left:0;top:334px;width:760px;height:116px;
      background:linear-gradient(90deg,#e6e0d3 0%,#d8d0bf 70%,rgba(190,170,130,.6) 100%)}
  .quote{left:40px;top:350px;width:600px;font-family:"Libre Baskerville",serif;font-style:italic;
      font-size:29px;line-height:44px;color:var(--ink);text-align:center}
  .offer-band{left:0;top:452px;width:760px;height:92px;
      background:linear-gradient(90deg,#5d4a2c 0%,#3a3426 55%,rgba(30,40,70,.7) 100%)}
  .offer{left:40px;top:458px;width:520px;text-align:center;font-family:"Montserrat",sans-serif;
      font-weight:600;font-size:28px;line-height:39px;color:var(--gold-bright)}
  .portrait{left:0;top:545px;width:405px;height:464px;
      background:radial-gradient(ellipse at 45% 35%,#5a4636 0%,#2a2a2e 45%,#161a26 100%)}
  .role{left:250px;width:310px;top:570px;text-align:center;font-family:"Libre Baskerville",serif;
      font-weight:700;font-size:26px;color:var(--cream)}
  .name{left:220px;width:370px;top:608px;text-align:center;font-family:"Libre Baskerville",serif;
      font-weight:700;font-size:37px;color:var(--gold)}
  .bio{left:250px;width:310px;top:663px;text-align:center;font-family:"Montserrat",sans-serif;
      font-weight:500;font-size:24px;line-height:35px;color:var(--cream)}
  .photo{left:690px;width:319px;border:2px solid var(--gold)}
  .photo-1{top:6px;height:224px;background:linear-gradient(160deg,#dfe3e6 0%,#8c97a8 50%,#2b3550 100%)}
  .photo-2{top:243px;height:240px;background:linear-gradient(160deg,#b98a5a 0%,#7d7b66 50%,#40503f 100%)}
  .photo-3{top:496px;height:274px;background:linear-gradient(160deg,#e3e5e8 0%,#a49a8e 50%,#3a3a48 100%)}
  .contact{left:470px;width:539px;text-align:center}
  .call{top:798px;font-family:"Montserrat",sans-serif;font-weight:500;font-size:26px;color:var(--cream)}
  .call b{font-weight:700;color:var(--gold-bright)}
  .phone{top:838px;display:flex;justify-content:center;align-items:center;gap:14px;
      font-family:"Montserrat",sans-serif;font-weight:700;font-size:44px;color:var(--gold-bright)}
  .email{top:906px;font-family:"Montserrat",sans-serif;font-weight:600;font-size:21px;color:var(--gold-bright)}
  .cash{left:830px;top:940px;width:179px;height:69px;
      background:linear-gradient(160deg,#6f7a62 0%,#c7cab1 60%,#8b8f78 100%);clip-path:polygon(30% 35%,100% 0,100% 100%,0 100%)}
</style>
</head>
<body>
  <div class="ad">
    <div class="abs brand-area"></div>
    <div class="abs brand"><span class="brand-dot"></span><span class="brand-name">Brightwater Ledger Services</span></div>
    <div class="abs rule" style="left:0;top:168px;width:680px"></div>

    <svg class="abs tick" width="60" height="70" viewBox="0 0 60 70" aria-hidden="true">
      <rect x="3" y="20" width="42" height="44" rx="5" fill="none" stroke="#d8b66a" stroke-width="5"/>
      <path d="M12 40 L24 54 L56 4" fill="none" stroke="#f0d693" stroke-width="7" stroke-linecap="round" stroke-linejoin="round"/>
    </svg>
    <div class="abs headline"><div class="l1">Tax, Accounting &amp;</div><div class="l2">Bookkeeping Services</div></div>

    <div class="abs rule" style="left:0;top:330px;width:680px"></div>
    <div class="abs quote-band"></div>
    <div class="abs quote">“We provide our services,<br>with you next mortgage in mind”</div>

    <div class="abs offer-band"></div>
    <div class="abs offer">Special pricing available for all<br>Mortgage Loan Customers!!</div>
    <div class="abs rule" style="left:0;top:542px;width:660px"></div>

    <div class="abs portrait" role="img" aria-label="Portrait of Marcus Delaney, President and CEO, in a dark hat and coat"></div>
    <div class="abs role">President / CEO</div>
    <div class="abs name">Marcus Delaney</div>
    <div class="abs bio">Primary service provider<br>with over 27 years<br>of experience</div>

    <div class="abs photo photo-1" role="img" aria-label="Advisors reviewing documents with a client"></div>
    <div class="abs photo photo-2" role="img" aria-label="Happy couple holding keys to their new home"></div>
    <div class="abs photo photo-3" role="img" aria-label="Two women working through finances with a calculator"></div>

    <svg class="abs" style="left:0;top:0" width="1009" height="1009" viewBox="0 0 1009 1009" aria-hidden="true">
      <path d="M660 0 C690 300 680 560 600 780 L1009 780" fill="none" stroke="#d8b66a" stroke-width="5"/>
      <path d="M385 782 C400 880 440 960 500 1009" fill="none" stroke="#f0d693" stroke-width="4"/>
      <path d="M405 782 C422 875 465 955 530 1009" fill="none" stroke="#a8843f" stroke-width="2"/>
    </svg>

    <div class="abs cash" role="img" aria-label="Stack of banknotes"></div>

    <div class="abs contact call"><b>Call</b> directly for more information:</div>
    <div class="abs contact phone">
      <svg width="58" height="58" viewBox="0 0 58 58" aria-hidden="true">
        <circle cx="29" cy="29" r="26" fill="none" stroke="#f0d693" stroke-width="3"/>
        <path d="M20 15c2-1 4 0 5 2l2 5c1 2 0 3-1 4l-2 2c1 4 5 8 9 9l2-2c1-1 3-2 4-1l5 2c2 1 3 3 2 5l-1 3c-1 2-3 3-5 3C27 46 12 31 12 19c0-2 1-4 3-5z" fill="#f0d693"/>
      </svg>
      <span>(240) 555-0182</span>
    </div>
    <div class="abs contact email">mdelaney@brightwaterledger-example.com</div>
  </div>
</body>
</html>
```